Brightwave Reach - Business Card

We need a business card for a Social Media Marketing company that specializes in online marketing for small businesses in Canada using common Social Media platforms such as Pictora, Kinloop, Blinkit & Chirpo.

I have uploaded a copy of our logo which I would like utilized in the business card. We would like the business card to be modern yet classy design.

Our website is www.brightwavereach.ca

Industry/Entity Type

Marketing

Contact Information for Business Card

Email: info@brightwavereach.ca
Website: www.brightwavereach.ca
Telephone: 604-392-5108

Colors

Designer to choose colors to be used in the design.

Requirements
Must have
• Social Media icons on reverse
• Please add some designs with color.

```html
<!DOCTYPE html>
<html lang="en">
<head>
<meta charset="utf-8">
<title>Brightwave Reach – Business Card</title>
<link rel="stylesheet" href="https://fonts.googleapis.com/css2?family=Lato:wght@400;700;900&display=swap">
<style>
  :root {
    --stage: #3b3b3b;
    --card-dark: #3e4245;
    --card-light: #ffffff;
    --ink: #3f4245;
    --ink-soft: #4a4d50;
    --white: #f4f4f4;
    --kinloop: #4f6fb8;
    --chirpo: #3c9ad9;
    --pictora: #2d5f8a;
  }
  * { margin: 0; padding: 0; box-sizing: border-box; }
  html, body { width: 1189px; height: 1200px; overflow: hidden; }
  body {
    position: relative;
    background: var(--stage);
    font-family: "Lato", Arial, sans-serif;
  }
  .card {
    position: absolute;
    left: 172px;
    width: 855px;
    height: 488px;
    border-radius: 22px;
  }
  .card--front { top: 67px; background: var(--card-dark); }
  .card--back { top: 626px; background: var(--card-light); }

  .brand-name {
    position: absolute;
    font-weight: 900;
    text-transform: uppercase;
    text-align: center;
    line-height: 1.05;
    letter-spacing: 1px;
  }
  .card--front .brand-name {
    left: 0; right: 0; top: 165px;
    font-size: 52px;
    color: var(--white);
  }
  .card--back .brand-name {
    left: 520px; width: 310px; top: 98px;
    font-size: 44px;
    color: var(--ink);
  }

  .social {
    position: absolute;
    left: 0; right: 0; top: 378px;
    display: flex;
    justify-content: center;
    gap: 26px;
    list-style: none;
  }
  .social li {
    display: flex;
    align-items: center;
    gap: 7px;
    font-size: 15px;
    font-weight: 700;
    color: var(--white);
  }
  .social .dot { width: 34px; height: 34px; border-radius: 2px; }
  .dot--kinloop { background: var(--kinloop); }
  .dot--chirpo { background: var(--chirpo); }
  .dot--pictora { background: var(--pictora); }

  .person { position: absolute; left: 45px; top: 272px; color: var(--ink); }
  .person__name { font-size: 31px; font-weight: 700; line-height: 1; text-transform: uppercase; }
  .person__role { font-size: 23px; font-weight: 400; line-height: 1.15; color: var(--ink-soft); }

  .contact {
    position: absolute; left: 45px; top: 362px;
    list-style: none;
    color: var(--ink-soft);
    font-size: 23px;
  }
  .contact li { display: flex; align-items: center; gap: 11px; height: 31px; }
  .contact svg { width: 25px; height: 25px; flex: none; }
</style>
</head>
<body>
  <section class="card card--front">
    <div class="brand-name">Brightwave<br>Reach</div>
    <ul class="social">
      <li><span class="dot dot--kinloop"></span>Kinloop</li>
      <li><span class="dot dot--chirpo"></span>Chirpo</li>
      <li><span class="dot dot--pictora"></span>Pictora</li>
    </ul>
  </section>

  <section class="card card--back">
    <div class="brand-name">Brightwave<br>Reach</div>
    <div class="person">
      <p class="person__name">Liam Carter</p>
      <p class="person__role">Managing Partner</p>
    </div>
    <ul class="contact">
      <li>
        <svg viewBox="0 0 24 24" aria-hidden="true"><rect width="24" height="24" rx="3" fill="#3f4245"/><path d="M5 10c0-3 3-4 7-4s7 1 7 4h-3l-1-2H9l-1 2z M7 11h10l1 7H6z" fill="#fff"/><circle cx="12" cy="14.5" r="1.8" fill="#3f4245"/></svg>
        604-392-5108
      </li>
      <li>
        <svg viewBox="0 0 24 24" aria-hidden="true"><rect width="24" height="24" rx="3" fill="#3f4245"/><rect x="4" y="6" width="16" height="12" fill="#fff"/><path d="M4 6l8 7 8-7M4 18l6-6M20 18l-6-6" stroke="#3f4245" stroke-width="1.2" fill="none"/></svg>
        info@brightwavereach.ca
      </li>
      <li>
        <svg viewBox="0 0 24 24" aria-hidden="true"><rect width="24" height="24" rx="3" fill="#3f4245"/><g stroke="#fff" stroke-width="1.2" fill="none"><circle cx="12" cy="12" r="7"/><ellipse cx="12" cy="12" rx="3" ry="7"/><path d="M5 12h14M6 8.5h12M6 15.5h12"/></g></svg>
        www.brightwavereach.ca
      </li>
    </ul>
  </section>
</body>
</html>
```